Neuartiges Verpackungsdesign für Erdnüsse mit Karamell in Puzzleform
Zielgruppe
Wir gründen eine Produktion für Lebensmittel. Es handelt sich hierbei um Erdnüsse mit Karamell. Unsere Zielgruppe ist von jung bis alt, beider Geschlechter.
Aufgabenstellung
Bei dem Produkt handelt es sich um eine Weiterentwicklung eines Klassikers. Es werden Nüsse mit Karamell überzogen und zu verschiedenen Formen verarbeitet, die Besonderheit liegt darin das durch ein neues technisches Verfahren ein höher Nussanteil erreicht wird und das Produkt zudem optisch schöner und geschmacklich leichter und knuspriger wirkt als bei der Konkurrenz.
Zudem wird Erdnussöl sowie verschiedene hochwertige Zusatzstoffe hinzugegeben, somit erhält das Produkt mehr ungesättigte Fettsäuren und ist zudem nicht nur ein gesunder sondern auch ein besonders schmackhafter Snack. Außerdem ist noch zu erwähnen das, dass Produkt vegan ist und glutenfrei. Zudem soll es als proteinreich deklariert werden, da mehr Erdnüsse und weniger Zucker dosiert werden.
Die größte Besonderheit ist jedoch das, dass Produkt in jeglicher Form gebracht werden kann. Es sind somit nicht nur quadratische oder Riegelartige Formen möglich. Die Formen reichen von Kreisen, Dreiecken bis zu Weihnachtsmänner und Osterhasen, aufgrund der Vielzahl der Formen welche möglich sind wird das Produkt “Tobble Crunchies“ genannt. Die Hauptform welche angestrebt wird, ist eine Puzzleform. Also es ist ein Snack welcher eine Puzzle Form besitzt.
Die Verpackung soll einen Klotzbodenbeutel darstellen, also eine Verpackung welche beispielsweise den Tam Tel‘s ähnelt. Die Maße der Verpackung sind 85mm in Breite, 160mm in Höhe und 65mm in Tiefe.
Das ganze Design sollte sehr modern sein und edel wirken, wie es beispielsweise bei hochwertigen Schokoladen wie bei Morwe der Fall ist, da in unseren Produkt hochwertiges Erdnussöl zum Einsatz kommt.
Zudem soll das Design nicht nur die mittlere bis ältere Generation ansprechen, sondern auch die Jugend mit dem Ziel sich gesünder zu ernähren und es sollen sogar Kinder angesprochen werden, da sehr viele Formen möglich sind und Kinder damit Puzzlen oder spielen könnten, so ähnlich wie es bei Wippfrucht von Wb..

```html
<!DOCTYPE html>
<html lang="de">
<head>
<meta charset="utf-8">
<title>Erdnuss-Karamell Bites – Verpackung</title>
<link rel="stylesheet" href="https://fonts.googleapis.com/css2?family=Bebas+Neue&family=Fira+Sans:wght@400&display=swap">
<style>
  :root {
    --backdrop: #221e1a;
    --bag-orange: #b8580c;
    --bag-band: #c8783c;
    --bag-peach: #dfa880;
    --label-white: #f1f0ef;
    --subtitle-band: #e4b08a;
    --ink-brown: #2e1610;
    --title-cream: #f5efe8;
    --caramel-dark: #9a5418;
    --caramel-mid: #c98543;
    --caramel-light: #dca064;
    --peanut-light: #f2d690;
  }
  * { margin: 0; padding: 0; box-sizing: border-box; }
  html, body { width: 1091px; height: 1200px; overflow: hidden; background: var(--backdrop); }
  .stage { position: relative; width: 1091px; height: 1200px; background: var(--backdrop); }
  .bag-front {
    position: absolute; left: 328px; top: 140px; width: 432px; height: 913px;
    background: var(--bag-orange); overflow: hidden; border-radius: 3px;
  }
  .bag-shapes { position: absolute; inset: 0; }
  .logo-slot {
    position: absolute; left: 117px; top: 86px; width: 206px; height: 63px;
    background: var(--label-white); display: flex; align-items: center; justify-content: center;
    font-family: "Fira Sans", sans-serif; font-size: 17px; color: var(--ink-brown); letter-spacing: 0.2px;
  }
  .product-title {
    position: absolute; left: 0; right: 0; top: 168px; text-align: center;
    font-family: "Bebas Neue", sans-serif; font-weight: 400; color: var(--title-cream);
    font-size: 61px; line-height: 58px; letter-spacing: 0.5px;
  }
  .product-subtitle {
    position: absolute; left: 25px; width: 384px; top: 295px; height: 31px;
    background: var(--subtitle-band); display: flex; align-items: center; justify-content: center;
    font-family: "Fira Sans", sans-serif; font-size: 18px; color: var(--ink-brown);
  }
  .product-visual { position: absolute; left: 0; top: 490px; width: 420px; height: 423px; }
  .claims {
    position: absolute; left: 258px; top: 422px; list-style: none;
    font-family: "Fira Sans", sans-serif; font-size: 22px; line-height: 29px; color: var(--ink-brown);
  }
  .claims li::before {
    content: ""; display: inline-block; width: 9px; height: 9px; border-radius: 50%;
    background: var(--ink-brown); margin-right: 9px; vertical-align: middle; position: relative; top: -2px;
  }
  .net-weight {
    position: absolute; left: 356px; top: 848px;
    font-family: "Bebas Neue", sans-serif; font-size: 38px; color: var(--ink-brown); letter-spacing: 0.5px;
  }
</style>
</head>
<body>
<main class="stage">
  <section class="bag-front">
    <svg class="bag-shapes" width="432" height="913" viewBox="0 0 432 913" aria-hidden="true">
      <path d="M0 421 C120 400 240 340 432 358 L432 913 L0 913 Z" fill="var(--bag-band)"/>
      <path d="M0 472 C130 430 260 400 432 402 L432 913 L0 913 Z" fill="var(--bag-peach)"/>
      <path d="M372 392 A88 88 0 1 1 230 452 M300 379 A88 88 0 0 1 350 380" fill="none" stroke="var(--ink-brown)" stroke-width="3.5" stroke-linecap="round"/>
    </svg>

    <div class="logo-slot">LOGO PLATZHALTER</div>

    <h1 class="product-title">Erdnuss-Karamell<br>Bites</h1>

    <p class="product-subtitle">Erdnusswürfel ummantelt in Karamell</p>

    <svg class="product-visual" role="img" aria-label="Illustration: große Erdnuss mit Erdnussstücken in einem spritzenden Strudel aus flüssigem Karamell" width="420" height="423" viewBox="0 0 420 423">
      <defs>
        <radialGradient id="caramel-swirl" cx="0.56" cy="0.36" r="0.7">
          <stop offset="0" stop-color="var(--peanut-light)"/>
          <stop offset="0.2" stop-color="var(--caramel-light)"/>
          <stop offset="0.55" stop-color="var(--caramel-mid)"/>
          <stop offset="1" stop-color="var(--caramel-dark)"/>
        </radialGradient>
      </defs>
      <path d="M0 18 C70 -4 150 8 220 30 C300 60 370 120 395 200 C415 270 380 330 300 350 C240 365 200 380 190 423 L0 423 Z" fill="url(#caramel-swirl)"/>
    </svg>

    <ul class="claims">
      <li>vegan</li>
      <li>proteinreich</li>
      <li>glutenfrei</li>
    </ul>

    <p class="net-weight">XX G</p>
  </section>
</main>
</body>
</html>
```